Australian Craft Distillery needs poster layout for its awesome Manifesto

Tall Finch's a small craft distillery based in the Brook Flats of Western Australia producing award-winning vodkas and gin. Check out our website www.tallfinchs-example.com.au to get a feel for our design aesthetic, especially from our bottle design. We are "Small Batch Liquors - Out of the Brook Flats". Everything we do reflects that.
We have a manifesto - The Tall Finch's Manifesto -that we proudly display in our tasting room, and was used as a basis for an artwork in our entry.
We've had a number of customers ask to buy a poster of the manifesto (attached) so I want to commission a more professional design than the current layout which was put together in Word! (yes I know, I'm sorry, I did move it into Illustrator later).
I think the text flows in a sequential order so I'm looking for a design that you read from start to finish rather than a random collection of statements. I'd like to include our logo in the design somewhere but it doesn't have to be front and centre. There is a secondary logo device as well - the interlocked T and F on the label which could be used. I'm assuming the print will be simple black on either a plain background or a "craft background" similar to the labels. Our current fonts are SchmutzICG for text and VeneerTwo for headings. The label uses Haymaker and Gin-Rough.
Print size will be A3 (prefer the design to be to this proportion and portrait orientation) and bigger up to A1. We'll print the final design on the back of t-shirts for staff as well. If I was going to sum up our style in a couple of words it would be "intelligently irreverent" Have fun with this, I certainly did writing it!

```html
<!DOCTYPE html>
<html lang="en">
<head>
<meta charset="utf-8">
<title>The Tall Finch's Manifesto</title>
<link href="https://fonts.googleapis.com/css2?family=Anton&family=Barlow+Semi+Condensed:wght@500&family=Special+Elite&display=swap" rel="stylesheet">
<style>
  :root {
    --kraft: #c6a585;
    --ink: #1c1916;
    --label: #f7f0e6;
  }
  html, body {
    margin: 0;
    padding: 0;
    overflow: hidden;
    background: var(--kraft);
  }
  .poster {
    position: relative;
    width: 849px;
    height: 1200px;
    background: var(--kraft);
    color: var(--ink);
    overflow: hidden;
  }
  .frame {
    position: absolute;
    inset: 0;
  }
  .title {
    position: absolute;
    top: 74px;
    left: 0;
    width: 100%;
    margin: 0;
    text-align: center;
    font-family: "Anton", sans-serif;
    font-weight: 400;
    font-size: 58px;
    line-height: 72px;
    letter-spacing: 0.5px;
    white-space: nowrap;
    text-transform: uppercase;
  }
  .subtitle {
    position: absolute;
    top: 148px;
    left: 86px;
    width: 678px;
    display: flex;
    align-items: center;
    gap: 10px;
    font-family: "Barlow Semi Condensed", sans-serif;
    font-weight: 500;
    font-size: 19px;
    letter-spacing: 1.6px;
    text-transform: uppercase;
    white-space: nowrap;
  }
  .subtitle::before,
  .subtitle::after {
    content: "";
    flex: 1;
    height: 2px;
    background: var(--ink);
    border-left: 2px solid var(--ink);
    border-right: 2px solid var(--ink);
    box-sizing: border-box;
  }
  .manifesto {
    position: absolute;
    top: 199px;
    left: 0;
    width: 100%;
    text-align: center;
    font-family: "Special Elite", monospace;
    font-size: 18px;
    line-height: 30.4px;
  }
  .stage { margin: 0 0 30.4px; }
  .stage-label {
    margin: 0;
    color: var(--label);
  }
  .stage p { margin: 0; white-space: nowrap; }
  .signoff {
    position: absolute;
    top: 1086px;
    left: 0;
    width: 100%;
    display: flex;
    justify-content: center;
    align-items: center;
    gap: 8px;
    font-family: "Special Elite", monospace;
    font-size: 17px;
  }
  .signoff-dot {
    width: 10px;
    height: 10px;
    border-radius: 50%;
    background: var(--ink);
  }
</style>
</head>
<body>
<main class="poster">
  <svg class="frame" width="849" height="1200" viewBox="0 0 849 1200" aria-hidden="true">
    <path d="M61 37 H788 A24 24 0 0 0 812 61 V1138 A24 24 0 0 0 788 1162 H61 A24 24 0 0 0 37 1138 V61 A24 24 0 0 0 61 37 Z"
          fill="none" stroke="#1c1916" stroke-width="3"/>
  </svg>

  <h1 class="title">The Tall Finch's Manifesto</h1>
  <div class="subtitle">Our thoughts on life, a.k.a. how to be better</div>

  <section class="manifesto">
    <div class="stage">
      <h2 class="stage-label" style="font-size:inherit;font-weight:400">first...</h2>
      <p>Work Smart. Love Hard. Play Often. Sleep More.</p>
      <p>Stay Present. Be Loca. Embrace Silly. Get Dirty (but) Stay Clean.</p>
      <p>Laugh. Cry. Run. Dance. Sing.</p>
      <p>Stop That (and) Slow down.</p>
    </div>
    <div class="stage">
      <h2 class="stage-label" style="font-size:inherit;font-weight:400">then...</h2>
      <p>Celebrate others success. Don’t be shit.</p>
      <p>Have one thing you are awesome at.</p>
      <p>Get off your phone. Show some fucking passion.</p>
      <p>Make something. Making money doesn’t count. Making babies does.</p>
      <p>Never stop exploring, never stop learning, share that with others.</p>
      <p>We all fuck up. Make good, learn, be better and move on.</p>
      <p>Life is far too short, squeeze every drop out of it and, of course...</p>
      <p>Drink better.</p>
    </div>
    <div class="stage">
      <h2 class="stage-label" style="font-size:inherit;font-weight:400">and finally...</h2>
      <p>Sometimes you just won’t understand.</p>
      <p>An argument is not a fight.</p>
      <p>You are not as important as you think.</p>
      <p>You are more loved than you think.</p>
      <p>Its ok to do things alone.</p>
      <p>Its ok not to be busy.</p>
      <p>There is no good reason to do a half arsed job.</p>
      <p>Teaching is the best way of learning.</p>
      <p>The past is important, what you do next is much more so.</p>
      <p>Change is inevitable, roll with it.</p>
      <p>Success is whatever you decide it to be.</p>
    </div>
  </section>

  <footer class="signoff">
    <span class="signoff-dot"></span>
    <span class="signoff-name">Tall Finch's</span>
  </footer>
</main>
</body>
</html>
```